Brenvick Holdings LLC, new Business cards

I'm moving offices and need new cards. Plus I'm open to modifying the current design of my card. I will keep the logo but would like to explore other layouts and fonts for the design. I've included the current double sided card for reference. I Like the navy color and white. Might be open to grays or silver. Needs to be clean and elegant.

Target Market(s)

Investors, buyers & sellers of private equities and real estate.

Contact Information for Business Card

Brenvick Holdings
Dorian P.K. Halvers, Managing Principal
418 Ostrander Ave., Suite 612
Denver, CO 80319
M: 970-555-0147, O: 303-555-0192
Dorian@brenvickholdings.example
Brenvickholdings.example

Colors
0354a2
ffffff
c4c4c4

Requirements
Must have
• Business card details.
• Logo raised or embossed, it was designed after a wax seal. Current has raised ink.
Nice to have
• Space on card to write additional notes.

```html
<!DOCTYPE html>
<html lang="en">
<head>
<meta charset="utf-8">
<title>Brenvick Holdings — Business Cards</title>
<link rel="stylesheet" href="https://fonts.googleapis.com/css2?family=Nunito+Sans:wght@300;400;600&display=swap">
<style>
  :root {
    --navy: #262a4e;
    --white: #ffffff;
    --silver: #c4c4c4;
    --seal-faint: #ecebef;
    --seal-faint-text: #d9d8de;
    --rule: #6b6d80;
    --backdrop: #e9e9ec;
  }
  * { margin: 0; padding: 0; box-sizing: border-box; }
  html, body { width: 1200px; height: 880px; overflow: hidden; }
  body {
    background: var(--backdrop);
    font-family: "Nunito Sans", sans-serif;
    position: relative;
  }
  .card {
    position: absolute;
    left: 280px;
    width: 640px;
    height: 366px;
    border-radius: 22px;
    background: var(--white);
    overflow: hidden;
    box-shadow: 0 6px 20px rgba(0,0,0,0.12);
  }
  .card--back { top: 40px; }
  .card--front { top: 466px; }

  /* Back: notes side */
  .back-seal {
    position: absolute;
    left: 195px; top: 48px;
    width: 250px; height: 250px;
    border-radius: 50%;
    background: var(--seal-faint);
    display: flex; align-items: center; justify-content: center;
  }
  .back-seal__name {
    color: var(--seal-faint-text);
    font-size: 22px;
    font-weight: 400;
    letter-spacing: 3px;
    text-transform: uppercase;
    text-align: center;
    line-height: 1.4;
  }
  .note-title {
    position: absolute;
    left: 0; right: 0; top: 34px;
    text-align: center;
    color: var(--navy);
    font-size: 20px;
    letter-spacing: 2px;
  }
  .note-lines {
    position: absolute;
    left: 70px; right: 70px; top: 72px;
  }
  .note-lines span {
    display: block;
    height: 32px;
    border-bottom: 1.5px dotted var(--rule);
  }
  .back-web {
    position: absolute;
    left: 0; right: 0; bottom: 26px;
    text-align: center;
    color: var(--navy);
    font-size: 17px;
  }

  /* Front: contact side */
  .front-mark {
    position: absolute;
    left: 0; top: 0;
    width: 252px; height: 366px;
    display: flex; flex-direction: column; align-items: center; justify-content: center;
    gap: 14px;
  }
  .front-mark__dot {
    width: 30px; height: 30px; border-radius: 50%;
    background: var(--navy);
  }
  .front-mark__name {
    color: var(--navy);
    font-size: 19px;
    font-weight: 600;
    letter-spacing: 2px;
    text-transform: uppercase;
    text-align: center;
    line-height: 1.35;
  }
  .front-panel {
    position: absolute;
    left: 252px; top: 0; right: 0; bottom: 0;
    background: var(--navy);
    border-left: 8px solid var(--silver);
    color: var(--white);
    padding: 58px 0 0 40px;
  }
  .person__name {
    font-size: 22px;
    font-weight: 400;
    letter-spacing: 1.5px;
    text-transform: uppercase;
  }
  .person__title { font-size: 15px; font-weight: 300; margin-top: 2px; }
  .contact { font-size: 15px; font-weight: 300; line-height: 1.42; margin-top: 20px; }
  .contact .gap { margin-top: 14px; }
</style>
</head>
<body>

<section class="card card--back" aria-label="Card back with note lines">
  <div class="back-seal"><span class="back-seal__name">Brenvick<br>Holdings</span></div>
  <div class="note-title">NOTE</div>
  <div class="note-lines">
    <span></span><span></span><span></span><span></span><span></span><span></span><span></span>
  </div>
  <div class="back-web">Brenvickholdings.example</div>
</section>

<section class="card card--front" aria-label="Card front with contact details">
  <div class="front-mark">
    <div class="front-mark__dot"></div>
    <div class="front-mark__name">Brenvick<br>Holdings</div>
  </div>
  <div class="front-panel">
    <h1 class="person__name">Dorian P.K. Halvers</h1>
    <div class="person__title">Managing Principal</div>
    <div class="contact">
      <p>418 Ostrander Ave., Suite 612</p>
      <p>Denver, CO 80319</p>
      <p class="gap">M: 970-555-0147</p>
      <p>O: 303-555-0192</p>
      <p>E: Dorian@brenvickholdings.example</p>
      <p class="gap">Brenvickholdings.example</p>
    </div>
  </div>
</section>

</body>
</html>
```